Industrial Inspection & Testing Company Needs Brochure

We need a brochure design for a company based in Western Pennsylvania, USA. Our company performs services mainly in industrial sites. These can include manufacturing, health & medical, power generation, and more. We use infrared thermography, vibration analysis, ultrasonic thickness testing, dynamic balancing and other practices to provide predictive maintenance to our customers. Please see our website for a more thorough explanation of our services. www.korbalinspect.com

Complete list of services:

Infrared Thermal Imaging
Vibration Analysis
High Temperature Video & Photography
High Speed Video
Laser Alignment
Dynamic Balancing
Motor Meggering
Leak Detection
Ultrasonic Thickness Testing
Oil Analysis

KTR, LLC - P.O. Box 4837 - Maplewick Township, PA 16239
Phone: 724-583-1149 / Fax: 724-583-1157

MISSION

KTR, LLC will provide the highest quality, cost effective, world class PdM services in the industry. Our commitment to continuing education and growth will afford our engineers the tools needed to stay on the cutting edge of technology. We believe in the implementation of Predictive Maintenance services to increase overall equipment reliability, reduce costs and improve profitability. Our goal is to provide continuous improvements to these processes. The company will network with various industry professionals to offer the widest range of equipment, training and reliability services available. Meeting these goals will ensure the company’s longevity and allow our valued customers to achieve the cost reduction goals that are needed in today’s competitive marketplace.
HISTORY
KTR, LLC was founded in March 1984, which emerged from the Greyhollow Alloy Works’ Development Laboratory, Monroeville, Pennsylvania. Its founders headed the Thermography and Photoinstrumentation Department of that facility.
While at the G. A. Works Development Laboratory, they established the utilization of thermography as a valuable tool for evaluating equipment and facilities in the steel industry. Their work set the standards for the use of thermography in the steel industry that continues today with KTR. Although the original thermographic equipment was crude, bulky and slow, KTR has maintained its position as an industry leader. Today KTR uses the most technologically advanced infrared systems available for on-site nondestructive industrial inspections.
In addition, while at G. A. Works Development, the founders of KTR pioneered the use of photographic cameras and high-speed motion pictures as another form of a predictive and preventative maintenance tool. Specially constructed camera systems with thermal protective housings were developed for inspecting blast furnace interior stockline armor areas, stove domes, and other high-temperature areas.
Today KTR remains on the cutting-edge in providing a wide range of nondestructive inspection services to industry.

***All of the photos and documents attached were either shot by us or purchased stock photos***

I realize that only a few images might be used, I just wanted to upload many to give designers a broad range to choose from.

Target Market(s)

Large industrial customers who use large amounts of electricity, heavy duty machinery, or both.

Industry/Entity Type

Industrial

Requirements
Must have
• Need a 3 full page tri-fold design (not skinny column tri-fold)

Contact information for our company, list of our services, our logo (possible redesign of logo), photos from our inspections that will be attached.
Nice to have
• List of services, breif explanation of each with graphical representation, contact information

```html
<!DOCTYPE html>
<html lang="en">
<head>
<meta charset="utf-8">
<title>KTR, LLC Tri-fold Brochure</title>
<link href="https://fonts.googleapis.com/css2?family=Marcellus+SC&family=Open+Sans:wght@400;600;700&display=swap" rel="stylesheet">
<style>
  :root {
    --stage: #2b2b2b;
    --paper: #ffffff;
    --cream: #fdf6d6;
    --ink: #2a2a2a;
    --red: #e31b23;
    --yellow: #ffd200;
    --orange: #f07a1c;
    --orange-deep: #e0561a;
    --navy: #1f2d8c;
    --gold: #f2c200;
    --sans: "Open Sans", Arial, sans-serif;
    --serif: "Marcellus SC", Georgia, serif;
  }
  * { box-sizing: border-box; margin: 0; padding: 0; }
  html, body { width: 785px; height: 1200px; overflow: hidden; background: var(--stage); }
  body { position: relative; font-family: var(--sans); color: var(--ink); }

  .spread { position: absolute; left: 22px; width: 740px; height: 581px; background: var(--paper); overflow: hidden; box-shadow: 0 4px 14px rgba(0,0,0,.5); }
  .spread--outside { top: 12px; }
  .spread--inside { top: 607px; }
  .abs { position: absolute; }
  .photo { position: absolute; }
  .wave { position: absolute; left: 0; display: block; }

  .copy { position: absolute; font-size: 9.6px; line-height: 15.4px; text-align: justify; }
  .copy--mid { font-size: 8.6px; line-height: 15.6px; }

  .flap-rule { position: absolute; height: 2px; background: var(--yellow); }

  .brand { position: absolute; display: flex; align-items: center; gap: 7px; font-family: var(--sans); font-weight: 700; color: var(--navy); letter-spacing: 1px; }
  .brand__dot { border-radius: 50%; background: var(--gold); }
  .brand--lg { font-size: 40px; }
  .brand--lg .brand__dot { width: 20px; height: 20px; }
  .brand--md { font-size: 32px; }
  .brand--md .brand__dot { width: 16px; height: 16px; }

  .address { position: absolute; left: 245px; width: 247px; top: 466px; text-align: center; font-size: 10.5px; line-height: 18px; }
  .address__web { font-weight: 700; font-size: 10px; }

  .tagline { position: absolute; font-family: var(--serif); color: var(--yellow); line-height: 1.05; }
  .tagline__big { font-size: 1.55em; }

  .footer-bar { position: absolute; background: var(--red); color: #fff; font-weight: 700; font-size: 10px; display: flex; align-items: center; justify-content: center; }

  .heading { position: absolute; font-family: var(--serif); font-size: 17px; letter-spacing: 1px; color: #111; }
  .body-text { position: absolute; font-size: 8.1px; line-height: 10.6px; text-align: justify; }
  .history-text { font-size: 7.9px; line-height: 10.1px; }
  .history-text p { margin: 0; }

  .services { position: absolute; left: 270px; top: 254px; list-style: none; font-family: var(--serif); font-size: 11px; line-height: 22.2px; color: #222; }
  .services li::before { content: "•"; margin-right: 6px; color: #333; }

  .inside-footer-web { position: absolute; right: 60px; top: 548px; color: #fff; font-size: 10px; font-weight: 700; }
</style>
</head>
<body>

<!-- Outside spread -->
<section class="spread spread--outside">
  <!-- back flap -->
  <div class="photo" role="img" aria-label="Cooling towers of a power plant at dusk" style="left:0;top:0;width:245px;height:200px;background:linear-gradient(180deg,#1f2a55 0%,#3c4f8c 45%,#c7834c 78%,#2a2218 100%);"></div>
  <svg class="wave" style="top:170px" width="245" height="40" viewBox="0 0 245 40"><path d="M0 18 Q120 40 245 6 L245 40 L0 40Z" fill="#fff"/><path d="M0 18 Q120 40 245 6" stroke="var(--yellow)" stroke-width="2" fill="none"/></svg>
  <p class="copy" style="left:10px;top:212px;width:228px;">Lorem Ipsum is simply dummy text of the printing and typesetting industry. Lorem Ipsum has been the industry's standard dummy text ever since the 1500s, when an unknown printer took a galley of type and scrambled it to make a type specimen book. It has survived not only five centuries, but also the leap into electronic typesetting, remaining essentially unchanged. It was popularised in the 1960s with the release of Typeleaf sheets containing Lorem Ipsum passages, and more recently with desktop publishing software like Quillset Composer including versions of Lorem Ipsum.</p>
  <div class="flap-rule" style="left:0;top:446px;width:245px;"></div>
  <div class="photo" role="img" aria-label="Row of cooling towers under a blue sky" style="left:0;top:456px;width:245px;height:125px;background:linear-gradient(180deg,#5b8fcf 0%,#a9c8e6 55%,#d9dde0 72%,#4d6a2e 100%);"></div>

  <!-- middle panel -->
  <div class="abs" style="left:245px;top:0;width:247px;height:581px;background:var(--cream);"></div>
  <p class="copy copy--mid" style="left:258px;top:8px;width:222px;">&nbsp;&nbsp;Lorem Ipsum is simply dummy text of the printing and typesetting industry. Lorem Ipsum has been the industry's standard dummy text ever since the 1500s, when an unknown printer took a galley of type and scrambled it to make a type specimen book. It has survived not only five centuries, but also the leap into electronic typesetting, remaining essentially unchanged. It was popularised in the 1960s with the release of Typeleaf sheets containing Lorem Ipsum passages, and more recently with desktop publishing software like Quillset Composer including versions of Lorem Ipsum.</p>
  <div class="brand brand--lg" style="left:318px;top:388px;"><span class="brand__dot"></span>KTR</div>
  <div class="address">
    P.O. Box 4837,<br>Maplewick Township<br>PA 16239<br>P : 724-583-1149 &nbsp;|&nbsp; F : 724-583-1157<br>
    <span class="address__web">Log On www.korbalinspect.com</span>
  </div>

  <!-- front cover -->
  <div class="photo" role="img" aria-label="Steel refinery towers against a clear sky" style="left:492px;top:0;width:248px;height:300px;background:linear-gradient(180deg,#7fb2e0 0%,#b7d4ec 55%,#8a8f94 80%,#5b5e62 100%);"></div>
  <svg class="wave" style="left:492px;top:262px" width="248" height="140" viewBox="0 0 248 140"><path d="M0 30 Q110 -4 248 20 L248 140 L0 140Z" fill="var(--red)"/><path d="M0 30 Q110 -4 248 20" stroke="var(--yellow)" stroke-width="3" fill="none"/></svg>
  <div class="tagline" style="left:508px;top:318px;font-size:17px;">FOR PDM...<br><span class="tagline__big">KTR</span> IS THE ONE!</div>
  <div class="photo" role="img" aria-label="Close-up of machine gears beside a thermal image" style="left:492px;top:396px;width:248px;height:86px;background:linear-gradient(90deg,#6d6a66 0%,#a8a29a 45%,#c54fd0 70%,#3d5cf0 100%);"></div>
  <div class="abs" style="left:492px;top:482px;width:248px;height:63px;background:#fff;"></div>
  <div class="brand brand--md" style="left:570px;top:490px;"><span class="brand__dot"></span>KTR</div>
  <div class="footer-bar" style="left:492px;top:550px;width:248px;height:31px;">Log On www.korbalinspect.com</div>
</section>

<!-- Inside spread -->
<section class="spread spread--inside">
  <div class="photo" role="img" aria-label="Blast furnace plant with stacks and pipework" style="left:0;top:0;width:245px;height:200px;background:linear-gradient(180deg,#9fc3e6 0%,#c9dbe9 40%,#6c5a4a 75%,#3a2f27 100%);"></div>
  <div class="photo" role="img" aria-label="Steel mill structure under cloudy sky" style="left:245px;top:0;width:247px;height:200px;background:linear-gradient(180deg,#d7dde3 0%,#a89a8c 50%,#6b4b38 100%);"></div>
  <div class="photo" role="img" aria-label="Electrical substation with high voltage equipment" style="left:492px;top:0;width:248px;height:200px;background:linear-gradient(180deg,#e4ecf2 0%,#b7c2ca 50%,#6d7780 100%);"></div>
  <svg class="wave" style="top:110px" width="740" height="120" viewBox="0 0 740 120"><path d="M0 120 L0 90 Q260 70 430 40 Q600 10 740 22 L740 120Z" fill="#fff"/><path d="M0 90 Q260 70 430 40 Q600 10 740 22" stroke="#bfbfbf" stroke-width="2" fill="none"/></svg>

  <h2 class="heading" style="left:14px;top:228px;">MISSION</h2>
  <p class="body-text" style="left:14px;top:252px;width:222px;">KTR, LLC will provide the highest quality, cost effective, world class PdM services in the industry. Our commitment to continuing education and growth will afford our engineers the tools needed to stay on the cutting edge of technology. We believe in the implementation of Predictive Maintenance services to increase overall equipment reliability, reduce costs and improve profitability. Our goal is to provide continuous improvements to these processes. The company will network with various industry professionals to offer the widest range of equipment, training and reliability services available. Meeting these goals will ensure the company’s longevity and allow our valued customers to achieve the cost reduction goals that are needed in today’s competitive marketplace.</p>

  <h2 class="heading" style="left:262px;top:218px;font-size:14px;">COMPLETE LIST OF SERVICES</h2>
  <ul class="services">
    <li>Infrared Thermal Imaging</li>
    <li>Vibration Analysis</li>
    <li>High Temperature Video &amp;</li>
    <li>Photography</li>
    <li>High Speed Video</li>
    <li>Laser Alignment</li>
    <li>Dynamic Balancing</li>
    <li>Motor Meggering</li>
    <li>Leak Detection</li>
    <li>Ultrasonic Thickness Testing</li>
    <li>Oil Analysis</li>
  </ul>

  <h2 class="heading" style="left:502px;top:152px;">HISTORY</h2>
  <div class="body-text history-text" style="left:502px;top:172px;width:228px;">
    <p>KTR, LLC was founded in March 1984, which emerged from the Greyhollow Alloy Works’ Development Laboratory, Monroeville, Pennsylvania. Its founders headed the Thermography and Photoinstrumentation Department of that facility.</p>
    <p>While at the G. A. Works Development Laboratory, they established the utilization of thermography as a valuable tool for evaluating equipment and facilities in the steel industry. Their work set the standards for the use of thermography in the steel industry that continues today with KTR. Although the original thermographic equipment was crude, bulky and slow, KTR has maintained its position as an industry leader. Today KTR uses the most technologically advanced infrared systems available for on-site nondestructive industrial inspections.</p>
    <p>In addition, while at G. A. Works Development, the founders of KTR pioneered the use of photographic cameras and high-speed motion pictures as another form of a predictive and preventative maintenance tool. Specially constructed camera systems with thermal protective housings were developed for inspecting blast furnace interior stockline armor areas, stove domes, and other high-temperature areas.</p>
    <p>Today KTR remains on the cutting-edge in providing a wide range of nondestructive inspection services to industry.</p>
  </div>

  <svg class="wave" style="top:488px" width="740" height="93" viewBox="0 0 740 93"><defs><linearGradient id="band" x1="0" x2="1"><stop offset="0" stop-color="var(--orange)"/><stop offset="1" stop-color="var(--orange-deep)"/></linearGradient></defs><path d="M0 12 Q300 40 500 30 Q640 24 740 42 L740 93 L0 93Z" fill="url(#band)"/><path d="M0 30 Q90 20 180 44 Q210 70 190 93 L0 93Z" fill="#fff"/></svg>
  <div class="brand brand--md" style="left:40px;top:530px;"><span class="brand__dot"></span>KTR</div>
  <div class="tagline" style="left:270px;top:536px;font-size:13px;">FOR PDM...<br><span class="tagline__big">KTR</span> IS THE ONE!</div>
  <div class="inside-footer-web">Log On www.korbalinspect.com</div>
</section>

</body>
</html>
```